Halloway Crest Backers Guild business cards

Create a single-sided business card for the Halloway Crest Backers Guild based on the attached logo.
The additional data fields include Name, Title, Email, Phone, and website.
Please use the following as sample data:
Name: Dean Varrow
Title: Co-Founder / Investor
Email: deanvarrow@mailtern.net
Phone: 555-314-2706
Website: www.hcbackersguild.com

Target Market(s)

Start ups, entrepreneurs, venture capitalists

Industry/Entity Type

Investment

Contact Information for Business Card

Professional business card. Technology company.

Font styles to use
Serif
Sans Serif

Requirements
Must have
• Include the HCBG logo (attached)
• Name
• Title
• Email
• Phone
• Website
Should not have
• Cute, cartoony

```html
<!DOCTYPE html>
<html lang="en">
<head>
<meta charset="utf-8">
<title>Halloway Crest Backers Guild – Business Card</title>
<link rel="stylesheet" href="https://fonts.googleapis.com/css2?family=Open+Sans:wght@400;600&family=Roboto:wght@400;700&display=swap">
<style>
  :root {
    --page-bg: #e6e3df;
    --card-white: #ffffff;
    --brand-green: #0b9a4a;
    --card-black: #1c1c1c;
    --ink-dark: #3a3a3a;
    --ink-light: #ffffff;
    --ink-contact: #f2f2f2;
  }
  * { margin: 0; padding: 0; box-sizing: border-box; }
  html, body {
    width: 1200px; height: 800px; overflow: hidden;
    background: var(--page-bg);
  }
  .business-card {
    position: absolute; left: 150px; top: 150px;
    width: 900px; height: 500px;
    background: var(--card-white);
    overflow: hidden;
    box-shadow: 0 4px 14px rgba(0,0,0,0.18);
    font-family: "Roboto", Arial, sans-serif;
  }
  .card-bands {
    position: absolute; inset: 0; width: 100%; height: 100%;
  }
  .brand-lockup {
    position: absolute; left: 92px; top: 72px;
    display: flex; align-items: center; gap: 30px;
  }
  .brand-mark {
    width: 72px; height: 72px; background: var(--brand-green);
  }
  .brand-name {
    font-family: "Open Sans", Arial, sans-serif;
    font-weight: 600; font-size: 38px; line-height: 1.12;
    color: var(--ink-dark); letter-spacing: 0.2px;
  }
  .holder {
    position: absolute; left: 70px; top: 250px;
    display: flex; align-items: flex-start; gap: 10px;
    color: var(--ink-light);
  }
  .holder-icon { width: 18px; height: 18px; margin-top: 26px; }
  .holder-name { font-weight: 700; font-size: 33px; line-height: 1.1; }
  .holder-title { font-weight: 400; font-size: 20px; line-height: 1.2; }
  .contact-list {
    position: absolute; left: 573px; top: 343px;
    list-style: none; color: var(--ink-contact);
    font-size: 20px;
  }
  .contact-item {
    display: flex; align-items: center; gap: 14px;
    height: 35px;
  }
  .contact-icon { width: 18px; height: 18px; flex: none; }
</style>
</head>
<body>
  <div class="business-card">
    <svg class="card-bands" viewBox="0 0 592 328" preserveAspectRatio="none" aria-hidden="true">
      <rect x="0" y="155" width="592" height="70" fill="var(--brand-green)"/>
      <path d="M592 160 L345 160 C305 160 300 225 240 225 L0 225 L0 328 L592 328 Z" fill="var(--card-black)"/>
    </svg>

    <div class="brand-lockup">
      <div class="brand-mark"></div>
      <div class="brand-name">Halloway Crest<br>Backers Guild</div>
    </div>

    <div class="holder">
      <svg class="holder-icon" viewBox="0 0 16 16" aria-hidden="true">
        <circle cx="8" cy="5" r="3.5" fill="#fff"/>
        <path d="M1.5 16 C1.5 10.5 14.5 10.5 14.5 16 Z" fill="#fff"/>
      </svg>
      <div>
        <div class="holder-name">Dean Varrow</div>
        <div class="holder-title">Co-Founder / Investor</div>
      </div>
    </div>

    <ul class="contact-list">
      <li class="contact-item">
        <svg class="contact-icon" viewBox="0 0 24 24" aria-hidden="true">
          <path fill="var(--brand-green)" d="M6.6 10.8c1.4 2.8 3.8 5.1 6.6 6.6l2.2-2.2c.3-.3.7-.4 1-.2 1.1.4 2.3.6 3.6.6.6 0 1 .4 1 1V20c0 .6-.4 1-1 1C10.6 21 3 13.4 3 4c0-.6.4-1 1-1h3.5c.6 0 1 .4 1 1 0 1.3.2 2.5.6 3.6.1.3 0 .7-.2 1z"/>
        </svg>
        <span>555-314-2706</span>
      </li>
      <li class="contact-item">
        <svg class="contact-icon" viewBox="0 0 24 24" aria-hidden="true">
          <rect x="2" y="5" width="20" height="14" fill="var(--brand-green)"/>
          <path d="M2 5 L12 13 L22 5" fill="none" stroke="var(--card-black)" stroke-width="1.6"/>
        </svg>
        <span>deanvarrow@mailtern.net</span>
      </li>
      <li class="contact-item">
        <svg class="contact-icon" viewBox="0 0 24 24" aria-hidden="true">
          <g fill="none" stroke="var(--brand-green)" stroke-width="2">
            <circle cx="12" cy="12" r="9.5"/>
            <ellipse cx="12" cy="12" rx="4" ry="9.5"/>
            <path d="M2.5 12 H21.5 M4 7 H20 M4 17 H20"/>
          </g>
        </svg>
        <span>www.hcbackersguild.com</span>
      </li>
    </ul>
  </div>
</body>
</html>
```